Business Cards used to invite people to our church

We are a church and have need of a business card sized advertisement that allows our members to hand them out in order to invite people to the church. I need the front of the card to say "You're Invited" or "Come Check us out". with the service times on the back of the card later.
I have attached one of the OLD cards we have used in the past, but we want a complete makeover, into a more modern style that does not require the image.
I am also replacing the old logo with a newer "flat" logo which is attached.
Please use marketing colors. (blue or red or something that catches attention)
Create a card that DOES NOT have the picture of the two people on the front
The information on the sample card back is correct to go onto new card
Target Market(s)
anyone
Industry/Entity Type
Business
Contact Information for Business Card
sertice times and address information which you can get from the sample card I uploaded. It should have "You're Invited" or "Come Check us out" on the front of the card with out logo.

```html
<!DOCTYPE html>
<html lang="en">
<head>
<meta charset="utf-8">
<title>Harbor Light Fellowship – Service Times</title>
<link rel="stylesheet" href="https://fonts.googleapis.com/css2?family=Overpass:wght@300;400;700&family=Roboto+Condensed:wght@700&display=swap">
<style>
  :root {
    --paper: #ffffff;
    --brand-red: #be1e2d;
    --brand-blue: #27317a;
    --blue-light: #3d4a8e;
    --ink-light: #ffffff;
  }
  * { margin: 0; padding: 0; box-sizing: border-box; }
  html, body {
    width: 1200px; height: 1000px; overflow: hidden;
    background: var(--paper);
    font-family: "Overpass", "Helvetica Neue", Arial, sans-serif;
  }
  .card {
    position: absolute; left: 55px; top: 167px;
    width: 1089px; height: 637px;
    background: var(--paper);
  }
  .card-header {
    position: absolute; left: 0; top: 0; width: 100%; height: 221px;
    background: var(--brand-red);
    color: var(--ink-light);
    text-align: center;
  }
  .church-name {
    position: absolute; left: 0; right: 0; top: 56px;
    font-weight: 700; font-size: 42px; letter-spacing: 0.3px; line-height: 1;
  }
  .church-address, .church-phone {
    position: absolute; left: 0; right: 0;
    font-weight: 300; font-size: 31px; line-height: 1;
  }
  .church-address { top: 116px; }
  .church-phone { top: 160px; }
  .worship-photo {
    position: absolute; left: 0; top: 230px; width: 100%; height: 407px;
    background:
      radial-gradient(ellipse at 50% 0%, rgba(90,104,170,0.55), rgba(39,49,122,0) 60%),
      linear-gradient(180deg, var(--blue-light) 0%, var(--brand-blue) 55%, var(--brand-blue) 100%);
  }
  .service-list { position: absolute; inset: 0; }
  .service {
    position: absolute; top: 326px; width: 170px; height: 202px;
    color: var(--ink-light);
  }
  .service svg { position: absolute; left: 0; top: 0; overflow: visible; }
  .service-label {
    position: absolute; left: 22px; top: 34px;
    font-size: 28px; font-weight: 400; white-space: nowrap; line-height: 1;
  }
  .service-label sup { font-size: 15px; vertical-align: 12px; }
  .service-time {
    position: absolute; left: 85px; top: 153px;
    font-family: "Roboto Condensed", "Arial Narrow", sans-serif;
    font-weight: 700; font-size: 25px; line-height: 1; white-space: nowrap;
  }
  .service--first { left: 178px; }
  .service--second { left: 438px; }
  .service--bible { left: 718px; }
</style>
</head>
<body>
<main class="card">
  <header class="card-header">
    <h1 class="church-name">Harbor Light Fellowship</h1>
    <p class="church-address">2480 W. Cedar Lane – Millbrook, TX 75990</p>
    <p class="church-phone">1–800–555–0192</p>
  </header>

  <div class="worship-photo" role="img" aria-label="Blue-toned photo of a congregation with hands raised in worship"></div>

  <section class="service-list">
    <div class="service service--first">
      <svg width="170" height="202" viewBox="0 0 170 202" fill="none" stroke="#fff" aria-hidden="true">
        <path d="M168 2 H2 V200 H168" stroke-width="4"/>
        <path d="M74 172 A33 33 0 1 1 107 139" stroke-width="7" stroke-linecap="round"/>
        <path d="M74 121 V139 H63" stroke-width="5"/>
      </svg>
      <p class="service-label">1<sup>st</sup> Service</p>
      <p class="service-time">9:00am</p>
    </div>

    <div class="service service--second">
      <svg width="170" height="202" viewBox="0 0 170 202" fill="none" stroke="#fff" aria-hidden="true">
        <path d="M168 2 H2 V200 H168" stroke-width="4"/>
        <path d="M74 172 A33 33 0 1 1 107 139" stroke-width="7" stroke-linecap="round"/>
        <path d="M74 121 V139 H63" stroke-width="5"/>
      </svg>
      <p class="service-label">2<sup>nd</sup> Service</p>
      <p class="service-time">11:00am</p>
    </div>

    <div class="service service--bible">
      <svg width="170" height="202" viewBox="0 0 170 202" fill="none" stroke="#fff" aria-hidden="true">
        <path d="M168 2 H2 V200 H168" stroke-width="4"/>
        <path d="M74 172 A33 33 0 1 1 107 139" stroke-width="7" stroke-linecap="round"/>
        <path d="M74 121 V139 H63" stroke-width="5"/>
      </svg>
      <p class="service-label">Wed. Bible class</p>
      <p class="service-time">11:00am</p>
    </div>
  </section>
</main>
</body>
</html>
```